Illustration: Content Marketing
Zielgruppe
Die Agentur Herr Bolt+++ bietet strategische Kommunikationsberatung und PR für Unternehmen, die im Internet Erfolg haben und sichtbarer werden möchten.
Seit 2008 berät sie schwerpunktmäßig Werbetechnologie-Unternehmen aus Deutschland, UK und den USA. Die Online-Expertise der Agentur wird auch von vielen Consumer-Brands geschätzt, die das Internet als Vertriebskanal nutzen. Einen besonderen Fokus legt Herr Bolt+++ auf Vertriebs-PR und Studien-PR, um für die Kunden messbare Erfolge zu erzielen.
Die inhabergeführte Agentur mit Sitz in Hamburg gehörte laut Netz Markt Journal zu den „5 PR-Agenturen to Watch 2011“.
Zu den Kunden der Agentur zählen Internet-Unternehmen, Start-ups und Online-Shops wie clickmeister, pulsmeter, brightloop, Falcon Gateway, kühlbote und Neighbour Circle.
Unsere Zielgruppe sind Werbefach-Medien wie Netz Markt Journal und Planen und Gewinnen und Wirtschaftsmedien wie Handelsrundschau, NKB, Nordländische Rundschau, Bote, Radar.
Aufgabenstellung
Für journalistische Artikel rund um das Thema Content Marketing im Internet suchen wir eine universelle Illustration. Gezeichnet, designt oder fotografiert –das überlassen wir Ihnen.
Content-Marketing bezeichnet eine Kommunikationsstrategie, um mittels nutzwertigen aber nicht werblichen Informationen, wie beispielsweise Fachartikel oder Studien, die Bekanntheit einer Marke oder eines Unternehmens bei der gewünschten Zielgruppe zu steigern, das Image zu verbessern oder neue Kunden zu gewinnen. So können auch komplexe Themen vermittelt werden, der potenzielle Kunde besser informiert und Bedürfnisse geweckt werden.
Wir beschreiben in den Artikeln, für die wir ein Bild suchen, den Aspekt für werbungtreibenden Unternehmen und erklären Firmen, wie Content Marketing verwendet werden kann.
Die Verwendung des Bildes ist sowohl für das Web als auch für Print-Magazine gedacht. Die Auflösung brauchen wir daher in 72dpi und 300 dpi.

```html
<!DOCTYPE html>
<html lang="de">
<head>
<meta charset="utf-8">
<title>Die besten Pflegeprodukte 2015</title>
<link rel="stylesheet" href="https://fonts.googleapis.com/css2?family=Questrial&family=Work+Sans:wght@600&display=swap">
<style>
  :root {
    --page-bg: #e8e7e5;
    --header-green: #a9b918;
    --nav-ink: #3c4a12;
    --heading-ink: #6f6f6f;
    --body-ink: #6a6a6a;
    --divider: #c9c8c5;
    --social-blue: #4a6aa8;
    --social-red: #a33a2a;
  }
  * { box-sizing: border-box; margin: 0; padding: 0; }
  html, body { width: 1200px; height: 801px; overflow: hidden; }
  body {
    background: var(--page-bg);
    font-family: "Questrial", Arial, sans-serif;
    color: var(--body-ink);
  }
  .site { position: relative; width: 1200px; height: 801px; }
  .site-header {
    position: absolute; left: 0; top: 0; width: 1200px; height: 110px;
    background: var(--header-green);
  }
  .main-nav {
    position: absolute; left: 300px; top: 42px;
    display: flex; gap: 20px;
    font-family: "Work Sans", Arial, sans-serif; font-weight: 600;
    font-size: 18px; line-height: 24px; color: var(--nav-ink);
  }
  .brand-name {
    position: absolute; right: 34px; top: 42px;
    font-size: 20px; line-height: 24px; color: var(--nav-ink);
  }
  .sidebar-divider {
    position: absolute; left: 254px; top: 140px; width: 1px; height: 661px;
    background: var(--divider);
  }
  .follow {
    position: absolute; left: 40px; top: 548px;
    font-size: 12px; line-height: 16px; color: var(--body-ink);
  }
  .social-icons { display: flex; gap: 6px; margin-top: 6px; }
  .social-icons span { width: 20px; height: 20px; background: var(--social-blue); }
  .social-icons span:last-child { background: var(--social-red); }
  .article-title {
    position: absolute; left: 296px; top: 138px;
    font-size: 30px; line-height: 36px; font-weight: 400; color: var(--heading-ink);
  }
  .product-visual {
    position: absolute; left: 296px; top: 196px; width: 560px; height: 270px;
    background: linear-gradient(90deg, #c8762a 0%, #c8762a 14%, #2b2b2b 22%, #2b2b2b 34%, #d9d6ca 42%, #d9d6ca 54%, #5fc2c4 62%, #5fc2c4 76%, #b4954f 84%, #b4954f 100%);
    opacity: .85; border-radius: 4px;
  }
  .article-body {
    position: absolute; left: 296px; top: 496px; width: 856px;
    font-size: 17px; line-height: 32px; color: var(--body-ink);
  }
</style>
</head>
<body>
  <main class="site">
    <header class="site-header">
      <nav class="main-nav">
        <span>Politik</span><span>Sport</span><span>Unterhaltung</span><span>Technik</span><span>Wirtschaft</span>
      </nav>
      <span class="brand-name">Tagesblick</span>
    </header>

    <div class="sidebar-divider"></div>

    <aside class="follow">
      <p>Follow us</p>
      <div class="social-icons"><span></span><span></span><span></span></div>
    </aside>

    <h1 class="article-title">Die besten Pflegeprodukte 2015</h1>

    <div class="product-visual" role="img" aria-label="Produktfoto: fünf Pflegetuben in Orange, Schwarz, Creme, Türkis und Gold nebeneinander"></div>

    <article class="article-body">
      <p>But I must explain to you how all this mistaken idea of denouncing pleasure and praising pain was born and I will give you a complete account of the system, and expound the actual teachings of the great explorer of the truth, the master-builder of human happiness. No one rejects, dislikes, or avoids pleasure itself, because it is pleasure, but because those who do not know how to pursue pleasure rationally encounter consequences that are extremely painful. Nor again is there anyone who loves or pursues or desires to obtain pain of itself, because it is pain, but because occasionally circumstances occur in which toil and pain can procure him some great pleasure.</p>
    </article>
  </main>
</body>
</html>
```